Card design for orthopaedic surgeons working as The Brindlewood Orthopaedic Centre

Business cards, letterhead

Colors

Designer to choose colors to be used in the design.

Requirements
Must have
• Late addition.
• Cards letterhead must have logos of
• Corvane Federated Institute of Surgeons
• Meridale Orthopaedic Society
Nice to have
• Back of card to have space for appointment time to be added by hand and some blank space for writing incidental other notes.

```html
<!DOCTYPE html>
<html lang="en">
<head>
<meta charset="utf-8">
<title>The Brindlewood Orthopaedic Centre – Business Card</title>
<link rel="stylesheet" href="https://fonts.googleapis.com/css2?family=Montserrat:wght@400;500;600&display=swap">
<style>
  :root {
    --backdrop: #1f1f1f;
    --card: #ffffff;
    --navy: #2a2872;
    --sky: #4aa3df;
    --deep-blue: #1f4a72;
    --tan: #b59d7c;
    --ink: #1c2a3a;
    --rule: #8a84b0;
  }
  * { box-sizing: border-box; margin: 0; padding: 0; }
  html, body {
    width: 1200px; height: 1200px; overflow: hidden;
    background: var(--backdrop);
    font-family: "Montserrat", sans-serif;
  }
  .sheet {
    width: 1200px; height: 1200px;
    display: flex; flex-direction: column; align-items: center; justify-content: center;
    gap: 36px;
  }
  .card {
    position: relative;
    width: 1000px; height: 546px;
    background: var(--card);
    border-radius: 34px;
    overflow: hidden;
  }
  .wordmark {
    position: absolute;
    font-weight: 500;
    color: var(--deep-blue);
    white-space: nowrap;
    letter-spacing: 0.2px;
  }
  .card-back .wordmark { right: 60px; bottom: 58px; font-size: 32px; }
  .card-front .wordmark { right: 60px; top: 150px; font-size: 34px; }

  .holder { position: absolute; left: 70px; top: 66px; }
  .holder-name { font-size: 46px; font-weight: 600; color: var(--navy); line-height: 1.1; }
  .holder-name .surname { color: var(--sky); }
  .holder-role { font-size: 25px; font-weight: 400; color: var(--tan); margin-top: 2px; letter-spacing: 0.5px; }

  .divider {
    position: absolute; left: 60px; right: 60px; top: 300px;
    height: 1.5px; background: var(--rule);
  }
  .contact {
    position: absolute; left: 60px; top: 330px;
    list-style: none; font-size: 24px; color: var(--ink);
  }
  .contact li { display: flex; align-items: flex-start; gap: 14px; line-height: 32px; }
  .contact .icon { width: 28px; height: 28px; flex: none; margin-top: 2px; }
  .contact .no-icon { padding-left: 42px; }
</style>
</head>
<body>
<main class="sheet">
  <section class="card card-back" aria-label="Card back">
    <p class="wordmark">The Brindlewood Orthopaedic Centre</p>
  </section>

  <section class="card card-front" aria-label="Card front">
    <div class="holder">
      <p class="holder-name">Martin <span class="surname">Caldwell</span></p>
      <p class="holder-role">Managing director</p>
    </div>
    <p class="wordmark">The Brindlewood Orthopaedic Centre</p>
    <div class="divider"></div>
    <ul class="contact">
      <li>
        <svg class="icon" viewBox="0 0 28 28" aria-hidden="true"><circle cx="14" cy="14" r="14" fill="#4aa3df"/><path d="M10 8c1 0 1.5 2.5 1.8 3.4.2.6-1 1.4-.9 1.9.6 1.6 2 3 3.6 3.6.5.1 1.3-1.1 1.9-.9.9.3 3.4.8 3.4 1.8 0 1.3-1.3 2.4-2.6 2.2C12.5 19.5 8.5 15.5 7.8 10.6 7.6 9.3 8.7 8 10 8z" fill="#fff"/></svg>
        <span>5550142873</span>
      </li>
      <li>
        <svg class="icon" viewBox="0 0 28 28" aria-hidden="true"><circle cx="14" cy="14" r="14" fill="#4aa3df"/><rect x="7.5" y="9.5" width="13" height="9" rx="1" fill="#fff"/><path d="M7.8 10l6.2 4.8 6.2-4.8" fill="none" stroke="#4aa3df" stroke-width="1.3"/></svg>
        <span>martin@brindlewoodortho.example</span>
      </li>
      <li>
        <svg class="icon" viewBox="0 0 28 28" aria-hidden="true"><circle cx="14" cy="14" r="14" fill="#4aa3df"/><path d="M14 6.5a5.5 5.5 0 0 1 5.5 5.5c0 4-5.5 9.5-5.5 9.5S8.5 16 8.5 12A5.5 5.5 0 0 1 14 6.5z" fill="#fff"/><circle cx="14" cy="12" r="2" fill="#4aa3df"/></svg>
        <span>218 N. Harlow Lane</span>
      </li>
      <li class="no-icon"><span>Fenwick Tx 70841</span></li>
    </ul>
  </section>
</main>
</body>
</html>
```